Seeking Creative Design for Tiny Nest Rentals Van Wrap - Showcase Our Brand on the Move!

Car wrap design for VERLANCE TROTTER ECOFLUX GRANDE SET 2024
Company: Tiny Nest Rentals

We are a company that rents baby equipment to tourists visiting Los Cabos, Mexico.

I'd like for it to be clear to the viewer of this design what the company does. It should mention the categories of baby equipment that we cover: Cribs & Sleep, Toys & Activities, Car Seats & Strollers, High Chairs, Bath & Potty, and Luxury Baby Gear.

If possible use the Tagline: Make your Cabo vacation feel like home

Also if possible include the following testimonial with 5 stars: “Above and beyond! They made our family vacation a breeze.”

For the design use the colors and look & feel of our website, and our logo. See tinynestrentalsmx.com.

In general, we would not like the design to feel very saturated, meaning we do not want the white in the van to be completely covered. We like fresh, clean, and modern looks.

Our main Call to Action is for the user to visit the website and place their reservation online.

UPDATE: We would love to explore some design alternatives using images of the actual gear that we rent. I have attached some of them to play with.

UPDATE 2: I notice many designs emphasizing the phone number. It is ok to have the phone number but smaller, we prefer motivating people to go to our website instead of calling.

Target Market(s)

Tourists visiting Los Cabos, Mexico with their babies or small children.

Requirements
Must have
• Brand colors
Should not have
• Oversaturated

```html
<!DOCTYPE html>
<html lang="en">
<head>
<meta charset="utf-8">
<title>Tiny Nest Rentals – Van Wrap Side Panel</title>
<link href="https://fonts.googleapis.com/css2?family=Bebas+Neue&family=Oswald:wght@400;500&family=Montserrat:wght@500&family=Lato:ital@1&display=swap" rel="stylesheet">
<style>
  :root {
    --navy: #233a8a;
    --orange: #e8630f;
    --teal: #2a9cc8;
    --ink: #1f1f1f;
    --cream: #f3ead0;
    --paper: #ffffff;
    --star: #e8630f;
  }
  html, body {
    margin: 0;
    padding: 0;
    overflow: hidden;
    background: var(--paper);
  }
  .wrap-canvas {
    position: relative;
    width: 1200px;
    height: 675px;
    overflow: hidden;
    background: var(--paper);
  }
  .wrap-shapes {
    position: absolute;
    inset: 0;
  }
  .brand-square {
    position: absolute;
    left: 691px;
    top: 246px;
    width: 46px;
    height: 46px;
    background: var(--navy);
  }
  .brand-name {
    position: absolute;
    left: 596px;
    top: 304px;
    width: 240px;
    margin: 0;
    font-family: "Montserrat", sans-serif;
    font-weight: 500;
    font-size: 25px;
    line-height: 1;
    color: var(--ink);
    text-align: center;
    white-space: nowrap;
  }
  .website-pill {
    position: absolute;
    left: 605px;
    top: 354px;
    width: 212px;
    height: 33px;
    border-radius: 9px;
    background: var(--navy);
    color: var(--cream);
    font-family: "Bebas Neue", sans-serif;
    font-size: 24px;
    line-height: 35px;
    text-align: center;
    white-space: nowrap;
  }
  .category-list {
    position: absolute;
    left: 843px;
    top: 174px;
    margin: 0;
    padding: 0;
    list-style: none;
    font-family: "Oswald", sans-serif;
    font-weight: 400;
    font-size: 11px;
    line-height: 14px;
    text-transform: uppercase;
    color: var(--cream);
  }
  .category-list li::before {
    content: "\25C6";
    font-size: 6px;
    margin-right: 5px;
    vertical-align: 2px;
  }
  .category-list .is-accent { color: var(--orange); }
  .slogan {
    position: absolute;
    left: 892px;
    top: 286px;
    width: 160px;
    font-family: "Oswald", sans-serif;
    font-weight: 500;
    font-size: 15px;
    line-height: 18px;
    color: var(--cream);
    text-align: center;
    white-space: nowrap;
    transform: rotate(-45deg);
    transform-origin: center;
  }
  .review-stars {
    position: absolute;
    left: 440px;
    top: 341px;
    font-size: 18px;
    letter-spacing: 1px;
    color: var(--star);
    line-height: 1;
  }
  .review-bubble {
    position: absolute;
    left: 422px;
    top: 362px;
    width: 115px;
    height: 42px;
    margin: 0;
    box-sizing: border-box;
    border: 1px solid #666;
    border-radius: 8px;
    background: var(--paper);
    font-family: "Lato", sans-serif;
    font-style: italic;
    font-size: 8.8px;
    line-height: 13px;
    color: var(--ink);
    text-align: center;
    padding-top: 2px;
  }
</style>
</head>
<body>
<main class="wrap-canvas">
  <svg class="wrap-shapes" width="1200" height="675" viewBox="0 0 1200 675" aria-hidden="true">
    <polygon class="teal-triangle" points="513,336 363,486 660,486" fill="var(--teal)"/>
    <polygon class="navy-triangle" points="739,161 1029,161 895,313" fill="var(--navy)"/>
    <polygon class="orange-band" points="744,486 1036,196 1068,395 1068,486" fill="var(--orange)"/>
  </svg>

  <ul class="category-list">
    <li>Cribs &amp; Sleep</li>
    <li class="is-accent">Toys &amp; Activities</li>
    <li>Car Seats &amp; Strollers</li>
    <li class="is-accent">Bath &amp; Potty</li>
    <li>High Chairs</li>
    <li class="is-accent">Luxury Baby Gear</li>
  </ul>

  <div class="brand-square"></div>
  <h1 class="brand-name">Tiny Nest Rentals</h1>
  <div class="website-pill">TINYNESTRENTALSMX.COM</div>

  <div class="slogan">MAKE YOUR CABO<br>VACATION FEEL<br>LIKE HOME</div>

  <div class="review-stars" aria-label="5 stars">★★★★★</div>
  <blockquote class="review-bubble">“Above and beyond!<br>They made our family<br>vacation a breeze.”</blockquote>
</main>
</body>
</html>
```